New home maintenance business, on the back of business card i would like dot points of my services provided.
these include,
General household repairs and maintenance
Painting
Plankor/Plaster Repairs
Fencing
Gardening and landscaping
Cleaning and removals
Doors and windows
Hinges and Locks
Fly screen/ screen door Repairs
I like black,silver, red but ill leav it up to you guys as something may be better for business.. , would also it be possible to create a logo for me incorporating the K&T as i want to make up t shirts in future thankyou
Updates
i would also like to put Marco Tessani on the cards aswell please, and on back change painter to proffesional painter and decorator, please
i like alot of the designs sofar, i cant put my finger on wat 1 yet though!! cheers guys
Industry/Entity Type
Business
Contact Information for Business Card
K&T HOME MAINTENANCE SERVICES
Lenny Tessani 0498127654
ktmaintenance@mailvexa.com
ABN:71452038619
Look and feel
Each slider illustrates characteristics of the customer's brand and the style your logo design should communicate.

```html
<!DOCTYPE html>
<html lang="en">
<head>
<meta charset="utf-8">
<title>K&amp;T Home Maintenance Services – Business Card</title>
<link rel="stylesheet" href="https://fonts.googleapis.com/css2?family=Open+Sans:wght@600;700&family=PT+Sans:wght@700&family=Roboto+Condensed:wght@800&family=Ovo&family=Arimo:wght@700&display=swap">
<style>
  :root{
    --ink:#262626;
    --band:#424242;
    --green:#7dc50f;
    --teal:#b1dadc;
    --frame:#1e1e1c;
    --paper:#ffffff;
    --ghost:rgba(150,170,170,.35);
  }
  *{margin:0;padding:0;box-sizing:border-box}
  html,body{width:948px;height:1200px;overflow:hidden;background:var(--paper)}
  .canvas{position:relative;width:948px;height:1200px;border:1px solid var(--frame);overflow:hidden}
  .card{position:absolute;left:20px;width:908px}
  .card--front{top:18px;height:559px}
  .card--back{top:619px;height:561px}
  .card__frame{position:absolute;inset:0;width:100%;height:100%}
  .card__frame .outer{fill:var(--frame)}
  .card__frame .gap{fill:var(--paper)}
  .card__frame .panel{fill:var(--teal)}

  .brand-name{position:absolute;font-family:"Open Sans",sans-serif;font-weight:700;color:var(--ink);line-height:1;white-space:nowrap}
  .brand-name--front{left:78px;top:70px;font-size:104px;letter-spacing:-2px}
  .brand-name--small{right:68px;bottom:38px;font-size:46px;letter-spacing:-1px}
  .brand-dot{position:absolute;border-radius:50%;background:var(--green)}
  .brand-dot--front{left:300px;top:92px;width:26px;height:26px}

  .person{position:absolute;right:73px;top:108px;font-family:"Open Sans",sans-serif;font-weight:600;font-size:51px;color:var(--ink);line-height:1;letter-spacing:-.5px}
  .company-band{position:absolute;left:63px;top:264px;width:781px;height:51px;border-radius:26px;background:var(--band);
    display:flex;align-items:center;justify-content:center;font-family:"PT Sans",sans-serif;font-weight:700;font-size:33px;color:var(--green);letter-spacing:-.6px}
  .contact{position:absolute;right:73px;top:345px;text-align:right;font-family:"Arimo",sans-serif;font-weight:700;font-size:24px;color:var(--ink);line-height:54px}

  .services-title{position:absolute;left:0;right:0;top:66px;text-align:center;font-family:"Roboto Condensed",sans-serif;font-weight:800;font-size:60px;color:var(--ink);line-height:1;letter-spacing:-.5px;padding-right:34px}
  .services-ghost{position:absolute;left:232px;top:210px;font-family:"Open Sans",sans-serif;font-weight:700;font-size:250px;color:var(--ghost);line-height:1;letter-spacing:-8px}
  .service-list{position:absolute;list-style:none;font-family:"Ovo",serif;font-size:24px;color:var(--ink)}
  .service-list li{position:relative;height:55px;line-height:28px;padding-left:20px;white-space:nowrap}
  .service-list li::before{content:"";position:absolute;left:0;top:9px;width:11px;height:11px;border-radius:50%;background:var(--ink);box-shadow:0 0 0 2px var(--paper)}
  .service-list--left{left:38px;top:208px}
  .service-list--right{left:583px;top:213px}
  .service-list--right li{padding-left:16px}
</style>
</head>
<body>
<main class="canvas">

  <section class="card card--front" aria-label="Business card front">
    <svg class="card__frame" viewBox="0 0 908 559" aria-hidden="true">
      <polygon class="outer" points="32,0 876,0 908,32 908,527 876,559 32,559 0,527 0,32"/>
      <polygon class="gap" points="38,12 870,12 896,38 896,521 870,547 38,547 12,521 12,38"/>
      <polygon class="panel" points="42,20 866,20 888,42 888,517 866,539 42,539 20,517 20,42"/>
    </svg>
    <div class="brand-name brand-name--front">K&amp;T</div>
    <h1 class="person">Lenny Tessani</h1>
    <div class="company-band">K&amp;T HOME MAINTENANCE SERVICES</div>
    <address class="contact" style="font-style:normal">
      <div>ktmaintenance@mailvexa.com</div>
      <div>Mob:&nbsp; 0498127654</div>
      <div>ABN:71452038619</div>
    </address>
  </section>

  <section class="card card--back" aria-label="Business card back">
    <svg class="card__frame" viewBox="0 0 908 561" aria-hidden="true">
      <polygon class="outer" points="32,0 876,0 908,32 908,529 876,561 32,561 0,529 0,32"/>
      <polygon class="gap" points="38,12 870,12 896,38 896,523 870,549 38,549 12,523 12,38"/>
      <polygon class="panel" points="42,20 866,20 888,42 888,519 866,541 42,541 20,519 20,42"/>
    </svg>
    <div class="services-ghost" aria-hidden="true">K&amp;T</div>
    <h2 class="services-title">Services Provided</h2>
    <ul class="service-list service-list--left">
      <li>General household repairs and maintenance</li>
      <li>Plankor/Plaster Repairs</li>
      <li>Gardening and landscaping</li>
      <li>Fly screen/screen door Repairs</li>
    </ul>
    <ul class="service-list service-list--right">
      <li>Painting/Fencing</li>
      <li>Hinges and Locks</li>
      <li>Doors and windows</li>
      <li>Cleaning and removals</li>
    </ul>
    <div class="brand-name brand-name--small">K&amp;T</div>
  </section>

</main>
</body>
</html>
```